Townhome Multi-Family Property Exterior Sign

Hello. We are looking for a new design for our exterior pylon for for a multi-family housing property in Texas. The design will need to go on a new sign panel to replace the existing (see photo of existing). We are looking to see both modern and contemporary designs. Included the sign should be the name, Loma Brisa Townhomes and the web address www.lomabrisatownhomes.example.

Attached here is a PDF file of the proposed new sign shape. We are open to other shape ideas as well if your design would better suit a more rectangular shape.

Industry/Entity Type

Property

Font styles to use
Serif
Sans Serif

Colors
9bcb3c

Requirements
Must have
• Name of building: Loma Brisa Townhomes
• Website: www.lomabrisatownhomes.example
Nice to have
• Address: 420-530 Halvorsen Lane (only if it fits nicely)

```html
<!DOCTYPE html>
<html lang="en">
<head>
<meta charset="utf-8">
<title>Loma Brisa Townhomes – Exterior Sign</title>
<link rel="stylesheet" href="https://fonts.googleapis.com/css2?family=Limelight&family=Raleway:wght@400;700&display=swap">
<style>
  :root {
    --backdrop: #9a9999;
    --glow: #e6e6e6;
    --sign-green: #9bcb3c;
    --crest-green: #86b22f;
    --ink: #231f20;
  }
  html, body {
    margin: 0;
    padding: 0;
    width: 1200px;
    height: 644px;
    overflow: hidden;
    background: var(--backdrop);
  }
  .sign-canvas {
    position: relative;
    width: 1200px;
    height: 644px;
    background: radial-gradient(ellipse 300px 240px at 600px 200px, var(--glow) 0%, var(--backdrop) 100%);
  }
  .sign-art { display: block; }
  .post { fill: var(--ink); }
  .panel { fill: var(--sign-green); }
  .frame-band { fill: none; stroke: var(--ink); stroke-width: 11; stroke-linejoin: miter; }
  .frame-keyline { fill: none; stroke: var(--ink); stroke-width: 2; }
  .crest { fill: url(#crestTone); }
  .property-name {
    font-family: "Limelight", "Georgia", serif;
    font-size: 150px;
    fill: var(--ink);
  }
  .rule { fill: var(--ink); }
  .property-type {
    font-family: "Raleway", "Helvetica", sans-serif;
    font-weight: 700;
    font-size: 58px;
    fill: var(--ink);
  }
  .web-address {
    font-family: "Raleway", "Helvetica", sans-serif;
    font-weight: 400;
    font-size: 24px;
    fill: var(--ink);
  }
</style>
</head>
<body>
<main class="sign-canvas">
  <svg class="sign-art" width="1200" height="644" viewBox="0 0 1200 644" xmlns="http://www.w3.org/2000/svg">
    <defs>
      <radialGradient id="crestTone" cx="50%" cy="60%" r="60%">
        <stop offset="0%" stop-color="#86b22f"/>
        <stop offset="100%" stop-color="#9bcb3c"/>
      </radialGradient>
    </defs>

    <g class="posts">
      <rect class="post" x="96" y="252" width="44" height="392"/>
      <polygon class="post" points="86,256 118,240 150,256"/>
      <rect class="post" x="1058" y="250" width="44" height="394"/>
      <polygon class="post" points="1048,254 1080,234 1112,254"/>
    </g>

    <path class="panel" d="M140,604 V262 C260,258 340,232 392,202 L400,196 H800 L808,202 C860,232 940,258 1058,262 V604 Z"/>

    <path class="frame-band" d="M410,218 C360,248 280,272 157,280 V584 H1043 V280 C920,272 840,248 790,218"/>
    <path class="frame-keyline" d="M420,240 C370,272 300,298 174,304 V564 H1026 V304 C900,298 830,272 780,240"/>

    <g class="crest-area" role="img" aria-label="Decorative scrollwork crest ornament topping the sign">
      <path class="crest" d="M392,206 C380,180 400,168 432,170 C448,140 480,132 500,140 C520,116 540,110 550,118 C560,92 580,78 600,80 C620,78 640,92 650,118 C660,110 680,116 700,140 C720,132 752,140 768,170 C800,168 820,180 808,206 C760,222 650,226 600,224 C550,226 440,222 392,206 Z"/>
    </g>

    <text class="property-name" x="224" y="444" textLength="748" lengthAdjust="spacingAndGlyphs">Loma Brisa</text>
    <rect class="rule" x="224" y="487" width="238" height="6"/>
    <text class="property-type" x="476" y="506" textLength="472" lengthAdjust="spacingAndGlyphs">TOWNHOMES</text>
    <text class="web-address" x="600" y="551" text-anchor="middle">www.lomabrisatownhomes.example</text>
  </svg>
</main>
</body>
</html>
```